National Virtual CPA Firm needs post card design

Virtual CPA firm called "QUINDRA" needs a 5.5” x 8.5” post card designed to market our services to middle market mid-size american businesses. We provide Full Service Payroll (includes the processing of payroll, printing of checks and direct depositing, tax filing, and tax payments), Bookkeeping (Using their native systems, or ours), Contract CFO (with expense reduction analysis), Reporting services for business directors to make informed decisions, Capital Fundraising (Advice on seeking equity to help grow your business), and Taxes (Personal (1040), Partnership (1065), Corporate (1120, 1120S (Including Consolidated Returns)), Trust (1041) and Non-Profit (990)), including all affiliated state returns. One of our major selling points is our variety of experience, and our fast turn around times on projects.
This project specifically, I would like to highlight the bookkeeping services, but still want the tax and payroll services listed on the postcard.
I have uploaded the logo design for QUINDRA and would like a postcard that compliments the logo.
Company contact info is:
Quindra accounting services Inc
P.O. Box 4586
Great falls, MT 59471
(800) 362-9174
Www.quindra-example.com
Target Market(s)
Small to medium size businesses
Industry/Entity Type
Accounting

```html
<!DOCTYPE html>
<html lang="en">
<head>
<meta charset="utf-8">
<title>Quindra Postcard</title>
<link href="https://fonts.googleapis.com/css2?family=Josefin+Sans:wght@300;400;700&family=Montserrat:wght@500;600&display=swap" rel="stylesheet">
<style>
  :root {
    --bg: #ececec;
    --orange-light: #ffc516;
    --orange: #f7aa1c;
    --orange-deep: #e08d10;
    --green: #7cbf3c;
    --green-dark: #5ea52a;
    --ink: #1d1d1d;
    --white: #ffffff;
    --photo-a: #d9dde2;
    --photo-b: #7c8592;
  }
  * { margin: 0; padding: 0; box-sizing: border-box; }
  html, body { width: 1200px; height: 800px; overflow: hidden; background: var(--bg); }
  .canvas { position: relative; width: 1200px; height: 800px; }
  .postcard {
    position: absolute; top: 219px; width: 560px; height: 362px;
    background: var(--white); overflow: hidden;
    box-shadow: 0 6px 18px rgba(0,0,0,0.12);
    font-family: "Josefin Sans", sans-serif;
  }
  .postcard--front { left: 30px; }
  .postcard--back { left: 610px; }
  .postcard__art { position: absolute; inset: 0; width: 560px; height: 362px; }

  .brand-name {
    position: absolute; top: 26px; right: 40px;
    font-family: "Josefin Sans", sans-serif; font-weight: 400;
    font-size: 30px; letter-spacing: 1px; color: var(--ink);
  }

  .badge {
    position: absolute; left: 248px; top: 110px; width: 86px; height: 86px;
    display: flex; flex-direction: column; align-items: center; justify-content: center;
    color: var(--white); text-align: center;
  }
  .badge__main { font-weight: 700; font-size: 19px; letter-spacing: 3px; line-height: 1; }
  .badge__sub { font-weight: 300; font-size: 10px; letter-spacing: 2.5px; margin-top: 3px; }

  .pitch { position: absolute; left: 34px; top: 112px; }
  .pitch__lead {
    font-size: 10px; font-weight: 400; letter-spacing: 1.5px; color: var(--white);
    line-height: 1.35; text-transform: uppercase;
  }
  .pitch__headline {
    margin-top: 16px; font-size: 23px; font-weight: 700; letter-spacing: 3.5px;
    color: var(--ink); line-height: 1.15; text-transform: uppercase;
  }
  .pitch__headline span { display: block; }
  .pitch__headline .pitch__light { font-weight: 300; letter-spacing: 5px; }
  .pitch__rule { width: 64px; height: 4px; background: var(--white); margin-top: 12px; }

  .contact-band {
    position: absolute; left: 0; bottom: 18px; height: 30px;
    display: flex; align-items: center; justify-content: space-between;
    padding: 0 26px 0 30px; color: var(--white);
  }
  .postcard--front .contact-band { width: 440px; }
  .postcard--back .contact-band { width: 470px; }
  .contact-band__item { display: flex; flex-direction: column; line-height: 1; }
  .contact-band__item--right { align-items: flex-end; }
  .contact-band__label { font-size: 7px; letter-spacing: 1px; font-weight: 300; }
  .contact-band__value { font-size: 11.5px; letter-spacing: 2px; font-weight: 400; margin-top: 2px; }

  .services { position: absolute; left: 36px; top: 118px; }
  .services__title {
    display: flex; align-items: center; gap: 10px;
    font-size: 24px; letter-spacing: 6px; font-weight: 400; color: var(--green);
  }
  .services__list { list-style: none; margin-top: 10px; margin-left: 6px; }
  .services__item {
    display: flex; align-items: center; gap: 9px;
    font-family: "Montserrat", sans-serif; font-weight: 600; font-size: 9.5px;
    color: var(--ink); text-transform: uppercase; letter-spacing: 0.2px; line-height: 1.75;
  }
  .services__item svg { flex: none; }
</style>
</head>
<body>
<main class="canvas">

  <!-- Front side -->
  <section class="postcard postcard--front">
    <svg class="postcard__art" viewBox="0 0 560 362" aria-hidden="false">
      <defs>
        <linearGradient id="frontOrange" x1="0" y1="1" x2="1" y2="0">
          <stop offset="0" stop-color="var(--orange-light)"/>
          <stop offset="1" stop-color="var(--orange)"/>
        </linearGradient>
        <linearGradient id="frontPhoto" x1="0" y1="0" x2="1" y2="1">
          <stop offset="0" stop-color="var(--photo-a)"/>
          <stop offset="1" stop-color="var(--photo-b)"/>
        </linearGradient>
      </defs>
      <path d="M330,82 C420,72 500,62 560,56 V362 H352 C330,322 296,282 312,220 C326,160 312,112 330,82Z"
            fill="url(#frontPhoto)" role="img" aria-label="Photo of business people reviewing financial charts with a calculator and pen"/>
      <path d="M0,0 H262 C300,50 318,130 300,210 C286,270 318,320 350,362 H0Z" fill="url(#frontOrange)"/>
      <path d="M262,0 C300,50 318,130 300,210 C286,270 318,320 350,362" fill="none" stroke="var(--green)" stroke-width="7"/>
      <path d="M282,0 C318,50 334,130 318,210 C306,270 336,320 366,362" fill="none" stroke="var(--white)" stroke-width="3"/>
      <circle cx="291" cy="153" r="45" fill="var(--white)"/>
      <circle cx="291" cy="153" r="41" fill="var(--green)"/>
      <rect x="0" y="314" width="440" height="30" rx="15" fill="var(--green)"/>
      <rect x="0" y="314" width="20" height="30" fill="var(--green)"/>
    </svg>

    <div class="brand-name">QUINDRA</div>

    <div class="badge">
      <span class="badge__main">FAST</span>
      <span class="badge__sub">TURNING</span>
    </div>

    <div class="pitch">
      <p class="pitch__lead">One of our major<br>selling points is our</p>
      <h1 class="pitch__headline">
        <span>Variety of</span>
        <span>Experience,</span>
        <span>Fast Turn</span>
        <span class="pitch__light">Around</span>
      </h1>
      <div class="pitch__rule"></div>
    </div>

    <div class="contact-band">
      <div class="contact-band__item">
        <span class="contact-band__label">Visit</span>
        <span class="contact-band__value">www.quindra-example.com</span>
      </div>
      <div class="contact-band__item contact-band__item--right">
        <span class="contact-band__label">Call Us</span>
        <span class="contact-band__value">(800) 362-9174</span>
      </div>
    </div>
  </section>

  <!-- Back side -->
  <section class="postcard postcard--back">
    <svg class="postcard__art" viewBox="0 0 560 362">
      <defs>
        <linearGradient id="backOrange" x1="0" y1="0" x2="1" y2="1">
          <stop offset="0" stop-color="var(--orange-light)"/>
          <stop offset="1" stop-color="var(--orange-deep)"/>
        </linearGradient>
      </defs>
      <path d="M326,90 H560 V362 H470 C478,300 440,268 392,236 C330,196 300,150 326,90Z" fill="url(#backOrange)"/>
      <path d="M318,40 C290,110 300,180 380,232 C440,270 476,300 470,362" fill="none" stroke="var(--green)" stroke-width="7"/>
      <path d="M330,90 C306,150 330,196 392,236 C440,268 478,300 470,362" fill="none" stroke="var(--white)" stroke-width="3"/>
      <rect x="0" y="314" width="470" height="30" rx="15" fill="var(--green)"/>
      <rect x="0" y="314" width="20" height="30" fill="var(--green)"/>
    </svg>

    <div class="brand-name">QUINDRA</div>

    <div class="services">
      <h2 class="services__title">
        <svg width="18" height="18" viewBox="0 0 18 18" aria-hidden="true">
          <circle cx="9" cy="9" r="8" fill="none" stroke="var(--ink)" stroke-width="1.6"/>
          <path d="M5,8 a4,4 0 0 1 8,0" fill="none" stroke="var(--ink)" stroke-width="1.6"/>
          <rect x="3.6" y="7.5" width="2.2" height="3.6" rx="1" fill="var(--ink)"/>
          <rect x="12.2" y="7.5" width="2.2" height="3.6" rx="1" fill="var(--ink)"/>
        </svg>
        SERVICES
      </h2>
      <ul class="services__list">
        <li class="services__item"><svg width="7" height="9" viewBox="0 0 7 9"><path d="M1,1 L5,4.5 L1,8" fill="none" stroke="var(--green)" stroke-width="2"/></svg>Full service payroll</li>
        <li class="services__item"><svg width="7" height="9" viewBox="0 0 7 9"><path d="M1,1 L5,4.5 L1,8" fill="none" stroke="var(--green)" stroke-width="2"/></svg>Bookkeeping</li>
        <li class="services__item"><svg width="7" height="9" viewBox="0 0 7 9"><path d="M1,1 L5,4.5 L1,8" fill="none" stroke="var(--green)" stroke-width="2"/></svg>Contract CFO</li>
        <li class="services__item"><svg width="7" height="9" viewBox="0 0 7 9"><path d="M1,1 L5,4.5 L1,8" fill="none" stroke="var(--green)" stroke-width="2"/></svg>Reporting services for business</li>
        <li class="services__item"><svg width="7" height="9" viewBox="0 0 7 9"><path d="M1,1 L5,4.5 L1,8" fill="none" stroke="var(--green)" stroke-width="2"/></svg>Directors</li>
        <li class="services__item"><svg width="7" height="9" viewBox="0 0 7 9"><path d="M1,1 L5,4.5 L1,8" fill="none" stroke="var(--green)" stroke-width="2"/></svg>And taxes</li>
        <li class="services__item"><svg width="7" height="9" viewBox="0 0 7 9"><path d="M1,1 L5,4.5 L1,8" fill="none" stroke="var(--green)" stroke-width="2"/></svg>Corporate</li>
        <li class="services__item"><svg width="7" height="9" viewBox="0 0 7 9"><path d="M1,1 L5,4.5 L1,8" fill="none" stroke="var(--green)" stroke-width="2"/></svg>Including all affiliated state returns</li>
      </ul>
    </div>

    <div class="contact-band">
      <div class="contact-band__item">
        <span class="contact-band__label">Visit</span>
        <span class="contact-band__value">www.quindra-example.com</span>
      </div>
      <div class="contact-band__item contact-band__item--right">
        <span class="contact-band__label">Call Us</span>
        <span class="contact-band__value">(800) 362-9174</span>
      </div>
    </div>
  </section>

</main>
</body>
</html>
```